Wordpress Design Project

I now need a Wordpress theme for my new business.
The business offers consultancy on Information Management, Knowledge Management, Records Management and Document Management.
The winning designer must be able to set up the site for me on my webspace provided by Tallowbrook Hosting, or talk me through how to do this.
I already have a logo designed which you can see by viewing my profile on here. I am happy to send copies of the original artwork to bidders.
I recently sold my interest in a very similar business, and want a website similar to (but not the same as) the previous company (who are now my competition!) This website can be viewed at www.qardvane.com
Categories will be similar, but I would like everything to be as configurable as possible.
I have a strong preference for clean unfussy design.
I want original design please. Please no templates from free to use sites with stock images... no jigsaw pictures!!!!
Love this one... http://www.felquist.tv/
Please get in touch with any questions.
Updates
Project Deadline Extended
Reason: All of these are too generic (brief says no jigsaw puzzle images), or have copied QDV which is the COMPETITION - so I don't want the site to look like theirs
Project Deadline Extended
Reason: Please keep trying people
Business
Business

```html
<!DOCTYPE html>
<html lang="en">
<head>
<meta charset="utf-8">
<title>Harwick Professional Services</title>
<link href="https://fonts.googleapis.com/css2?family=Source+Sans+3:wght@400;600&display=swap" rel="stylesheet">
<style>
:root{
  --navy:#0f3f7d;
  --navy-dark:#0c2f63;
  --button:#1f82d6;
  --button-edge:#1666b0;
  --active:#35a9ea;
  --text:#1c1c1c;
  --rule-light:#3fa3ec;
  --panel-line:#9fc6e8;
  --frame:#c3dbf0;
  --footer-top:#6b6d70;
  --footer-bottom:#2f3134;
  --footer-bar:#242527;
  --footer-text:#ffffff;
}
*{margin:0;padding:0;box-sizing:border-box}
html,body{width:1200px;height:2228px;overflow:hidden;background:#fff}
body{position:relative;font-family:"Source Sans 3","Myriad Pro",Arial,sans-serif;color:var(--text)}
.abs{position:absolute}
.lines{white-space:nowrap}

/* header */
.brand{left:32px;top:30px;display:flex;align-items:center;gap:16px}
.brand-mark{width:89px;height:89px;border-radius:50%;background:var(--navy)}
.brand-name{font-size:48px;font-weight:600;color:var(--navy);letter-spacing:3px;line-height:1;margin-top:4px}
.brand-name small{display:block;font-size:13.5px;letter-spacing:5.6px;margin-top:4px}
.main-nav{right:52px;top:80px;display:flex;gap:22px;list-style:none}
.main-nav a{font-size:21.5px;color:var(--navy);text-decoration:none}
.main-nav a.current{color:var(--active);text-decoration:underline}
.header-band{left:0;top:160px;width:1200px;height:12px;background:var(--navy-dark);box-shadow:0 4px 5px rgba(0,0,0,.35)}

/* hero */
.hero-title{left:90px;top:268px;color:var(--navy);font-weight:600;font-size:43px;line-height:1.28}
.hero-title span{display:block;font-size:34px}
.btn{display:flex;align-items:center;justify-content:center;gap:10px;background:var(--button);border:1px solid var(--button-edge);color:#fff;font-size:21px;text-decoration:none}
.btn::after{content:"";border-left:9px solid #fff;border-top:6px solid transparent;border-bottom:6px solid transparent}
.hero-btn{left:358px;top:402px;width:134px;height:33px}
.hero-art{left:576px;top:252px;width:624px;height:318px;background:
  radial-gradient(ellipse 75% 60% at 78% 112%,#2f9ae6 0%,#5bb6ef 38%,#a9dbf7 62%,rgba(255,255,255,0) 80%),
  linear-gradient(115deg,#ffffff 20%,#e6f3fc 55%,#ffffff 90%)}
.hero-rule{left:0;top:569px;width:1200px;height:10px;background:linear-gradient(90deg,var(--rule-light),#64b8f0 50%,#2d8fe0)}

/* welcome */
.welcome{left:25px;top:604px;width:800px}
.welcome h1{font-size:28px;font-weight:400;color:var(--navy);line-height:36px;margin-bottom:3px}
.welcome p{font-size:16px;line-height:28.2px}
.welcome p.indent{text-indent:73px}
.welcome-btn{left:674px;top:979px;width:134px;height:33px}

/* recent projects */
.projects{left:851px;top:610px;width:333px;height:417px;border:1px solid var(--panel-line)}
.projects h2{position:absolute;left:12px;top:14px;font-size:28px;font-weight:400;color:var(--navy);line-height:36px}
.projects-art{position:absolute;left:15px;top:63px;width:303px;height:181px;border-radius:12px;border:3px solid #eaf3fb;background:radial-gradient(circle at 50% 50%,#efe6c8 0%,#dde8f1 28%,#c9dcec 60%,#eef5fb 100%);box-shadow:0 3px 5px rgba(0,0,0,.45)}
.projects h3{position:absolute;left:0;width:100%;top:256px;text-align:center;font-size:21px;font-weight:400;color:var(--navy);line-height:26px}
.projects p{position:absolute;left:23px;top:285px;font-size:16px;line-height:28px}
.projects-btn{position:absolute;left:177px;top:352px;width:134px;height:33px}

/* services */
.service{width:302px}
.service-art{width:302px;height:175px;border-radius:10px;border:3px solid var(--frame);box-shadow:0 4px 5px rgba(0,0,0,.45)}
.service h3{font-size:20px;font-weight:400;color:var(--navy);text-align:center;width:280px;margin-top:14px;line-height:28px}
.service p{font-size:16px;line-height:28.2px;margin:6px 0 0 4px}
.service .more{position:absolute;right:0;top:344px;font-size:15.5px;color:var(--text);text-decoration:none;line-height:28px}

/* footer */
.footer{left:0;top:1861px;width:1200px;height:303px;background:linear-gradient(var(--footer-top),var(--footer-bottom));color:var(--footer-text)}
.footer h4{font-size:15.5px;font-weight:400;position:absolute;top:23px;line-height:22px}
.footer ul{list-style:none;position:absolute}
.quick-links{left:46px;top:55px}
.quick-links li{font-size:12.5px;line-height:28px}
.story-list li,.news-list li{font-size:12.5px;position:relative;padding-left:22px;white-space:nowrap}
.story-list li::before,.news-list li::before{content:"";position:absolute;left:0;border-left:10px solid #fff;border-top:8px solid transparent;border-bottom:8px solid transparent}
.story-list{left:205px;top:55px}
.story-list li{line-height:27.8px;margin-bottom:11px}
.story-list li::before{top:6px}
.news-list{left:520px;top:60px}
.news-list li{line-height:21px;margin-bottom:21px}
.news-list li::before{top:3px}
.view-all{position:absolute;font-size:12.5px;line-height:18px}
.signup-text{position:absolute;left:890px;top:57px;font-size:12.5px;line-height:28.5px;white-space:nowrap}
.signup-field{position:absolute;left:890px;top:145px;width:258px;height:38px;background:#fff;border:2px solid #cfd0d2}
.signup-btn{position:absolute;left:1075px;top:200px;font-size:17px;display:flex;align-items:center;gap:12px}
.signup-btn::after{content:"";border-left:9px solid #fff;border-top:8px solid transparent;border-bottom:8px solid transparent}
.footer-bar{left:0;top:2164px;width:1200px;height:64px;background:var(--footer-bar);color:#fff;font-size:12.5px;text-align:center;line-height:62px;border-top:2px solid #1a1a1a}
</style>
</head>
<body>

<header>
  <div class="abs brand">
    <div class="brand-mark"></div>
    <div class="brand-name">HARWICK<small>PROFESSIONAL SERVICES</small></div>
  </div>
  <ul class="abs main-nav">
    <li><a class="current" href="#">Home</a></li>
    <li><a href="#">About Us</a></li>
    <li><a href="#">Services</a></li>
    <li><a href="#">Technology</a></li>
    <li><a href="#">News</a></li>
    <li><a href="#">Contact</a></li>
  </ul>
  <div class="abs header-band"></div>
</header>

<section class="hero">
  <h2 class="abs hero-title">Professional Services<span>for Business Management</span></h2>
  <a class="abs btn hero-btn" href="#">Read More</a>
  <div class="abs hero-art" role="img" aria-label="Illustration of two consultants standing on a glowing blue globe, surrounded by streams of binary data representing managed information"></div>
  <div class="abs hero-rule"></div>
</section>

<section class="abs welcome">
  <h1>Welcome to Harwick</h1>
  <p class="lines">Lorem Ipsum is simply dummy text of the printing and typesetting industry. Lorem Ipsum has been the industry's<br>standard dummy text ever since the 1500s, when an unknown printer took a galley of type and scrambled it to make<br>a type specimen book. It has survived not only five centuries, but also the leap into electronic typesetting, remaining<br>essentially unchanged. It was popularised in the 1960s with the release of Typeframe sheets containing Lorem Ipsum<br>passages, and more recently with desktop publishing software like Pageloom Press including versions of Lorem<br>Ipsum.</p>
  <p class="lines indent">Lorem Ipsum is simply dummy text of the printing and typesetting industry. Lorem Ipsum has been the<br>industry's standard dummy text ever since the 1500s, when an unknown printer took a galley of type and scrambled<br>it to make a type specimen book. It has survived not only five centuries, but also the leap into electronic typesetting,<br>remaining essentially unchanged. It was popularised in the 1960s with the release of Typeframe sheets containing<br>Lorem Ipsum passages, and more recently with desktop publishing software like Pageloom Press of Lorem Ipsum.</p>
</section>
<a class="abs btn welcome-btn" href="#">Read More</a>

<aside class="abs projects">
  <h2>Recent Projects</h2>
  <div class="projects-art" role="img" aria-label="Diagram of a collaborative records database at the centre, linked to stocks, quotation, orders, delivery, invoicing, purchases and accounting"></div>
  <h3>Project Title</h3>
  <p class="lines">Lorem Ipsum has been the industry's stand-<br>ard dummy text ever since the 1500s</p>
  <a class="btn projects-btn" href="#">Read More</a>
</aside>

<section class="services">
  <article class="abs service" style="left:39px;top:1072px">
    <div class="service-art" role="img" aria-label="Photo of a consultancy team seated around a meeting table with a laptop" style="background:linear-gradient(180deg,#eef1f4 0%,#c9ced6 45%,#3c4350 100%)"></div>
    <h3>Business Service</h3>
    <p class="lines">There are many variations of passages of<br>Lorem Ipsum available, but the majority<br>have suffered alteration in some form, by<br>injected humour</p>
    <a class="more" href="#">Read More&gt;&gt;</a>
  </article>
  <article class="abs service" style="left:456px;top:1072px">
    <div class="service-art" role="img" aria-label="Illustration of blue figures fitting large grey pieces together" style="background:linear-gradient(180deg,#f7f8f9 0%,#d7dde3 55%,#4a9be0 100%)"></div>
    <h3>Business Service</h3>
    <p class="lines">There are many variations of passages of<br>Lorem Ipsum available, but the majority<br>have suffered alteration in some form, by<br>injected humour</p>
    <a class="more" href="#">Read More&gt;&gt;</a>
  </article>
  <article class="abs service" style="left:860px;top:1072px">
    <div class="service-art" role="img" aria-label="Photo of a presenter mapping a process on a flip chart for a seated colleague" style="background:linear-gradient(90deg,#c7ccd4 0%,#f4f5f7 40%,#eceef1 70%,#59606b 100%)"></div>
    <h3>Business Service</h3>
    <p class="lines">There are many variations of passages of<br>Lorem Ipsum available, but the majority<br>have suffered alteration in some form, by<br>injected humour</p>
    <a class="more" href="#">Read More&gt;&gt;</a>
  </article>
  <article class="abs service" style="left:39px;top:1463px">
    <div class="service-art" role="img" aria-label="Diagram of a business process management cycle linking strategy, assessment, modelling, analysis, implementation and optimisation" style="background:radial-gradient(circle at 50% 50%,#4b4e53 0%,#4b4e53 24%,#1f5d8c 30%,#dfe8f0 44%,#f3f6f9 100%)"></div>
    <h3>Business Service</h3>
    <p class="lines">There are many variations of passages of<br>Lorem Ipsum available, but the majority<br>have suffered alteration in some form, by<br>injected humour</p>
    <a class="more" href="#">Read More&gt;&gt;</a>
  </article>
  <article class="abs service" style="left:456px;top:1463px">
    <div class="service-art" role="img" aria-label="Photo of consultants shaking hands over an agreement" style="background:linear-gradient(180deg,#f3f4f6 0%,#cfd3d9 40%,#2b2f36 100%)"></div>
    <h3>Business Service</h3>
    <p class="lines">There are many variations of passages of<br>Lorem Ipsum available, but the majority<br>have suffered alteration in some form, by<br>injected humour</p>
    <a class="more" href="#">Read More&gt;&gt;</a>
  </article>
  <article class="abs service" style="left:860px;top:1463px">
    <div class="service-art" role="img" aria-label="Illustration of colourful letter tiles spelling success, plan, idea and management on a grid" style="background:linear-gradient(180deg,#eef2f7 0%,#e3e9f1 30%,#e7a13c 55%,#cf3b35 75%,#eef2f7 100%)"></div>
    <h3>Business Service</h3>
    <p class="lines">There are many variations of passages of<br>Lorem Ipsum available, but the majority<br>have suffered alteration in some form, by<br>injected humour</p>
    <a class="more" href="#">Read More&gt;&gt;</a>
  </article>
</section>

<footer class="abs footer">
  <h4 style="left:46px">Quick Links</h4>
  <ul class="quick-links">
    <li>Home</li><li>Services</li><li>Technology</li><li>News</li><li>Contact</li>
  </ul>

  <h4 style="left:208px">Harwick Success Stories</h4>
  <ul class="story-list">
    <li>There are many variations of passages<br>of Lorem Ipsum available, but the majority<br>have suffered alteration in some form.</li>
    <li>There are many variations of passages<br>of Lorem Ipsum available, but the majority<br>have suffered alteration in some form</li>
  </ul>
  <span class="view-all" style="left:376px;top:240px">View All &gt;&gt;</span>

  <h4 style="left:526px">News &amp;Blogs</h4>
  <ul class="news-list">
    <li>This book is a treatise on the theory of ethics,<br>very popular during the Renaissance.</li>
    <li>This book is a treatise on the theory of ethics,<br>very popular during the Renaissance.</li>
    <li>This book is a treatise on the theory of ethics,<br>very popular during the Renaissance.</li>
  </ul>
  <span class="view-all" style="left:717px;top:237px">View All &gt;&gt;</span>

  <h4 style="left:890px">Newsletter Signup</h4>
  <p class="signup-text">Sign up and we'll keep you notified on any<br>announcements regarding changes to our<br>site or our products &amp; services</p>
  <div class="signup-field"></div>
  <span class="signup-btn">Sign up</span>
</footer>
<div class="abs footer-bar">© Harwick.com2012. All Rights Reserved .</div>

</body>
</html>
```